Rolling Nest - Portable Skateboard Display, Organizer, & Stand

Single Webpage for a new company that just launched our first product, the "Rolling Nest Skateboard Stand". This is a consumer product targeted toward parents (especially moms) with kids who have skateboards laying around. Our product is a storage/display/stand that keeps skateboards off of the ground and wheels away from walls. The website design needs to really sell the product as a Portable and Quality product, which can be put anywhere in the home. The website should appeal to adults (Moms especially) and help them quickly understand the versatility, flexibility, high quality, simplicity, and use of the Rolling Nest Skateboard stand. Our website can be viewed at www.rollingnest.example - we'd like to continue to link visitors to our Marketvale product listing for purchases (in the design you submit). Please review the attached creative files and feel free to reach out for additional information.

Target Market(s)

Parents (specifically Moms) with children who own skateboards, interested in keeping a clean and organized home.

Industry/Entity Type

It Company

Number of Pages Required

1 page

Font styles to use
Sans Serif

Requirements
Must have
• Must express the Portability, Quality, and Flexibility of the product. (It can be moved / placed anywhere, does not require mounting or drilling holes)
Nice to have
• Really sell the ease of use and benefit.
Should not have
• Should not be overly complex or cluttered.

```html
<!DOCTYPE html>
<html lang="en">
<head>
<meta charset="utf-8">
<title>Rolling Nest – Skateboard Stand</title>
<link href="https://fonts.googleapis.com/css2?family=Open+Sans:ital,wght@0,400;0,600;0,700;1,400&display=swap" rel="stylesheet">
<style>
:root{
  --blue:#1f5f9e;
  --blue-dark:#174a7c;
  --nav:#1b5593;
  --ink:#333;
  --muted:#777;
  --green:#5aa02c;
  --orange:#f0b36a;
  --line:#e3e3e3;
  --footer:#2b2b2b;
  --page:#ffffff;
}
*{box-sizing:border-box;margin:0;padding:0}
html,body{width:686px;height:1200px;overflow:hidden;background:var(--page)}
body{font-family:"Open Sans",Arial,sans-serif;color:var(--ink);position:relative}
.abs{position:absolute}

/* header */
.site-header{position:absolute;left:0;top:0;width:686px;height:64px}
.brand-name{position:absolute;left:40px;top:20px;font-weight:400;font-size:18px;line-height:24px;color:var(--ink);white-space:nowrap}
.cart{position:absolute;right:40px;top:24px;font-size:9px;color:#555;display:flex;align-items:center;gap:6px;font-weight:600}

.main-nav{position:absolute;left:0;top:64px;width:686px;height:21px;background:var(--nav)}
.main-nav ul{list-style:none;display:flex;margin-left:42px;height:100%}
.main-nav li{font-size:7.5px;font-weight:600;color:#fff;padding:0 18px;line-height:21px}
.main-nav li.active{background:var(--blue-dark)}

/* hero */
.hero{position:absolute;left:0;top:85px;width:686px;height:309px;
  background:linear-gradient(160deg,#9a9a9a 0%,#6e6e6e 45%,#4a4a4a 100%)}
.hero-offer{position:absolute;left:48px;top:150px;color:var(--orange);font-size:15px;line-height:19px;text-transform:uppercase;width:240px}
.hero-price{position:absolute;left:48px;top:196px;color:#fff;font-size:40px;font-weight:600}
.hero-arrow{position:absolute;top:135px}

/* sections */
.section-title{position:absolute;left:40px;font-size:16px;letter-spacing:.5px;text-transform:uppercase;color:#333;font-weight:600}
.section-title b{color:var(--blue);font-weight:600}

.product-card{position:absolute;top:453px;width:138px;height:199px;background:#fff;box-shadow:0 0 4px rgba(0,0,0,.15)}
.product-photo{position:absolute;left:18px;top:8px;width:102px;height:72px}
.product-name{position:absolute;left:14px;top:92px;font-size:10px;font-weight:700;color:#333}
.product-price{position:absolute;left:14px;top:106px;font-size:16px;font-weight:600;color:var(--green)}
.product-desc{position:absolute;left:14px;top:128px;width:112px;font-size:6.5px;line-height:8.5px;color:var(--muted)}
.btn{position:absolute;background:var(--blue);color:#fff;font-size:7px;font-weight:600;text-align:center;text-transform:uppercase}
.product-card .btn{left:14px;top:162px;width:58px;height:18px;line-height:18px}

.pager{position:absolute;top:671px;width:14px;height:14px;border-radius:50%;background:#888}

.video-copy{position:absolute;left:40px;width:300px;font-size:7px;line-height:10px;color:#666}
.video-frame{position:absolute;left:419px;top:806px;width:226px;height:110px;background:#cfcfcf}
.video-bar{position:absolute;left:0;top:0;width:100%;height:30px;background:var(--blue-dark)}
.video-bar span{position:absolute;left:32px;top:4px;font-size:8px;font-weight:700;color:#fff}
.video-thumb{position:absolute;left:0;top:30px;width:100%;height:80px;background:linear-gradient(120deg,#d9d4cc,#a9a49c)}

.reviews-title{position:absolute;left:0;top:970px;width:686px;text-align:center;font-size:16px;text-transform:uppercase;color:#333;font-weight:600}
.reviews-title b{color:var(--blue);font-weight:600}
.reviewer{position:absolute;left:298px;top:1008px;display:flex;align-items:center;gap:10px}
.avatar{width:38px;height:38px;border-radius:50%;background:#c9b9a6}
.reviewer-name{font-size:8px;font-weight:700;color:#333}
.quote{position:absolute;left:84px;top:1057px;width:520px;text-align:center;font-size:8px;line-height:11px;color:#555}
.quote i{color:var(--blue)}

/* footer */
.site-footer{position:absolute;left:0;top:1127px;width:686px;height:73px;background:var(--footer)}
.social{position:absolute;left:42px;top:14px;display:flex;gap:5px}
.social span{width:17px;height:17px;border-radius:50%;background:#555}
.social span:nth-child(1){background:#3b5998}
.social span:nth-child(2){background:#3aa5d8}
.social span:nth-child(3){background:#c7462f}
.social span:nth-child(4){background:#e98a2c}
.copyright{position:absolute;left:42px;top:48px;font-size:6px;color:#aaa}
.newsletter{position:absolute;left:494px;top:14px;font-size:7px;font-weight:600;color:#fff;text-transform:uppercase}
.newsletter-field{position:absolute;left:494px;top:34px;width:130px;height:15px;background:#fff;font-size:6px;color:#999;padding:4px}
.newsletter-go{position:absolute;left:624px;top:34px;width:20px;height:15px;background:#555}
</style>
</head>
<body>

<header class="site-header">
  <p class="brand-name">Rolling Nest</p>
  <div class="cart">
    <svg width="12" height="12" viewBox="0 0 12 12"><rect x="2" y="4" width="8" height="7" fill="#333"/><path d="M4 4V2.5a2 2 0 0 1 4 0V4" stroke="#333" fill="none"/></svg>
    MY CART (0) ITEM
  </div>
</header>

<nav class="main-nav">
  <ul>
    <li class="active">HOME</li><li>ABOUT US</li><li>PRODUCTS</li><li>WHOLESALE</li><li>VIDEOS</li><li>HAVE AN IDEA?</li><li>CONTACTS</li>
  </ul>
</nav>

<section class="hero" role="img" aria-label="Photo of a rider standing on a skateboard on a paved street">
  <svg class="hero-arrow" style="left:14px" width="14" height="26"><path d="M12 2 2 13l10 11" stroke="#fff" stroke-width="2" fill="none"/></svg>
  <svg class="hero-arrow" style="right:14px" width="14" height="26"><path d="M2 2l10 11L2 24" stroke="#fff" stroke-width="2" fill="none"/></svg>
  <p class="hero-offer">Free shipping for prime members and orders over</p>
  <p class="hero-price">$35!</p>
</section>

<h2 class="section-title" style="top:425px">Featured <b>Product</b></h2>

<article class="product-card" style="left:40px">
  <div class="product-photo" role="img" aria-label="Skateboard standing in a black stand" style="background:linear-gradient(#f2f2f2,#cfcfcf)"></div>
  <p class="product-name">PRODUCT NAME</p><p class="product-price">$19.50</p>
  <p class="product-desc">Consectetur adipiscing elit sed do eiusmod tempor</p>
  <span class="btn">Buy now</span>
</article>
<article class="product-card" style="left:197px">
  <div class="product-photo" role="img" aria-label="Skateboard standing in a red stand" style="background:linear-gradient(#f4f4f4,#e23a4a)"></div>
  <p class="product-name">PRODUCT NAME</p><p class="product-price">$19.50</p>
  <p class="product-desc">Consectetur adipiscing elit sed do eiusmod tempor</p>
  <span class="btn">Buy now</span>
</article>
<article class="product-card" style="left:354px">
  <div class="product-photo" role="img" aria-label="Skateboards in red and green stands" style="background:linear-gradient(90deg,#e23a4a,#7fcf3a)"></div>
  <p class="product-name">PRODUCT NAME</p><p class="product-price">$19.50</p>
  <p class="product-desc">Consectetur adipiscing elit sed do eiusmod tempor</p>
  <span class="btn">Buy now</span>
</article>
<article class="product-card" style="left:509px">
  <div class="product-photo" role="img" aria-label="Skateboard standing in a green stand" style="background:linear-gradient(#f4f4f4,#8fd03c)"></div>
  <p class="product-name">PRODUCT NAME</p><p class="product-price">$19.50</p>
  <p class="product-desc">Consectetur adipiscing elit sed do eiusmod tempor</p>
  <span class="btn">Buy now</span>
</article>

<span class="pager" style="left:327px"></span><span class="pager" style="left:344px;background:#555"></span>

<h2 class="section-title" style="top:752px">Featured <b>Video</b></h2>
<p class="video-copy" style="top:780px">Lorem ipsum dolor sit amet, consectetur adipiscing elit, sed do eiusmod tempor incididunt ut labore et dolore magna aliqua. Ut enim ad minim veniam, quis nostrud exercitation ullamco laboris nisi ut aliquip ex ea commodo consequat.</p>
<p class="video-copy" style="top:828px">Duis aute irure dolor in reprehenderit in voluptate velit esse cillum dolore eu fugiat nulla pariatur. Excepteur sint occaecat cupidatat non proident.</p>
<span class="btn" style="left:40px;top:872px;width:44px;height:18px;line-height:18px">View all</span>

<div class="video-frame">
  <div class="video-bar"><span>Rolling Nest Skateboard Stand</span></div>
  <div class="video-thumb" role="img" aria-label="Video still of a skateboard placed in the stand indoors"></div>
  <svg class="abs" style="left:6px;top:36px" width="22" height="14"><rect width="22" height="14" fill="#2a8fd6"/><path d="M8 3l7 4-7 4z" fill="#fff"/></svg>
</div>

<h2 class="reviews-title">
  <svg width="44" height="6" style="vertical-align:middle;margin-right:10px"><line x1="0" y1="3" x2="44" y2="3" stroke="#bbb"/></svg>Customer <b>Reviews</b><svg width="44" height="6" style="vertical-align:middle;margin-left:10px"><line x1="0" y1="3" x2="44" y2="3" stroke="#bbb"/></svg>
</h2>
<svg class="abs" style="left:270px;top:1020px" width="8" height="12"><path d="M7 1 2 6l5 5" stroke="#999" fill="none"/></svg>
<svg class="abs" style="left:406px;top:1020px" width="8" height="12"><path d="M1 1l5 5-5 5" stroke="#999" fill="none"/></svg>
<div class="reviewer"><span class="avatar" role="img" aria-label="Customer portrait"></span><span class="reviewer-name">JHON DOE</span></div>
<p class="quote"><i>"More Than 5 STARS"</i> – Perfect solution to the hazards of a loose skateboard. Well made and perfectly portable. I sent 3 as gifts and plan on buying more. Well made, great colors and takes up very little space. Plus at this price point you can have one in multiple locations.</p>

<footer class="site-footer">
  <div class="social"><span></span><span></span><span></span><span></span></div>
  <p class="copyright">Copyright 2014 Rolling Nest All Right Reserved</p>
  <p class="newsletter">Newsletter sign up</p>
  <div class="newsletter-field">Enter your Email</div>
  <div class="newsletter-go"></div>
</footer>

</body>
</html>
```